Larkmoor Capital Partners need a desert themed website!

We need a web design and development for our informational website for our new company named Larkmoor Capital Partners. We would like it to be desert themed and it can be color or black and white. We would like it to be classy and clean, while also talking to the benefits of investment partner with us.

We're thinking probably a home page with a nice image of a Scottsdale landscape, then other pages would What we offer our partners page (or other wording if you find something better), a meet the founder page, and a contact us page.

What we offer our partners (or other wording if you think of something better):
Our investors offer an opportunity to families that cannot usually get approved for a mortgage, to be able to become future homeowners. Thus, Benefiting both the investors and local surrounding community members. Our investors get to both have all the benefits of an investment with receiving above market rates of return to themselves and helping families find homes at the same time.

Maybe also build an infographic with these benefits: Safety, Security, Long-term investment horizon, cashflow, tax benefits, above market rate of return, and capital growth.

And a meet the founder page. With my headshot.

Dale Corwith is a private equity investor providing significantly above market returns to his investment partners while taking the time to be involved with his community and family. Dale first honed his skills in taking calculated risk decisions while very young where he took on playing poker professionally. He succeeded at the highest levels for over a decade competing in high stakes professional cash games around the world.

From the poker world he transitioned to investing in public and private markets. He took an approach of knowing the companies he invests in intimately and after over 10,000 hours of research became known in his community as the person to get investment advice on the electric vehicle industry for his voracious research and expert insight.

He now invests in single family homes in the Phoenix market using his past experience analyzing probabilistic outcomes and comparing the ROIs of different potential strategies. These skills have contributed to his success in investing in companies where he used his ability to assess risk to reward ratios to significantly outperform the market over an extended period.

Contact page we want my email Dale@LarkmoorFunds.example, my instagram: @DaleCorwith, and my linkedin https://www.profilehub.example/in/dale-corwith-58172036/

I have included my headshot for the about me page. I've included some saguaro generated images feel free to incorporate into the website (or make them the company logo), or not, whatever you feel gives the best look for the website.

```html
<!DOCTYPE html>
<html lang="en">
<head>
<meta charset="utf-8">
<title>Larkmoor Capital Partners</title>
<link rel="stylesheet" href="https://fonts.googleapis.com/css2?family=Poppins:wght@300;400;500;600&display=swap">
<style>
:root{
  --olive:#47421f;
  --olive-deep:#3d381a;
  --cream:#fffdf1;
  --white:#ffffff;
  --ink:#111111;
  --gold:#f0b84a;
  --line:#9d9a8a;
  --sand:#e9dfc0;
  --ring:#ecebe4;
}
*{box-sizing:border-box;margin:0;padding:0}
html,body{width:1200px;height:4351px;overflow:hidden}
body{font-family:'Poppins',sans-serif;color:var(--ink);background:var(--white);position:relative}
.abs{position:absolute}
.site-header{position:absolute;top:0;left:0;width:1200px;height:112px;background:var(--white)}
.brand{position:absolute;left:75px;top:42px;font-size:25px;font-weight:400;color:var(--olive-deep)}
.nav{position:absolute;top:58px;left:707px;display:flex;gap:32px;font-size:14.5px;color:var(--ink)}
.nav .active{color:var(--gold)}
.hero{position:absolute;top:112px;left:0;width:1200px;height:659px;background:var(--cream)}
.hero-kicker{position:absolute;left:106px;top:130px;font-size:27px;font-weight:500;color:var(--olive)}
.hero-title{position:absolute;left:103px;top:168px;font-size:70px;line-height:82px;font-weight:500;color:var(--ink);letter-spacing:1px}
.hero-sub{position:absolute;left:104px;top:326px;font-size:54px;font-weight:500}
.btn{position:absolute;background:var(--olive);color:var(--white);display:flex;align-items:center;justify-content:center;font-size:16px}
.hero-frame{position:absolute;left:585px;top:93px;width:515px;height:416px;background:var(--white);border-radius:40px 0 90px 0;box-shadow:0 2px 10px rgba(0,0,0,.05)}
.hero-art{position:absolute;left:13px;top:8px;width:495px;height:402px;border-radius:30px 0 80px 0;background:linear-gradient(180deg,#f2d9b4 0%,#e8b58d 35%,#c98a62 55%,#a7884f 75%,#8b7a48 100%)}
.dots{position:absolute;top:572px;left:550px;display:flex;gap:10px;align-items:center}
.dots span{width:11px;height:11px;border-radius:50%;background:#d0d0d0}
.dots .on{width:28px;height:6px;border-radius:3px;background:var(--olive)}
.about{position:absolute;top:771px;left:0;width:1200px;height:709px;background:var(--white)}
.photo-frame{position:absolute;left:148px;top:169px;width:382px;height:426px;background:var(--white);border-radius:0 0 50px 0;box-shadow:0 2px 12px rgba(0,0,0,.12)}
.photo-bg{position:absolute;left:10px;top:10px;width:362px;height:406px;background:var(--sand);border-radius:0 0 45px 0}
.photo{position:absolute;left:158px;top:67px;width:362px;height:518px;border-radius:90px 90px 45px 0;background:linear-gradient(180deg,#4a3a2e 0%,#b98a6d 30%,#c79a80 55%,#7b7570 80%,#77726c 100%)}
.section-head{color:var(--olive);font-weight:500}
.rule{position:absolute;height:2px;background:var(--line)}
.rule::before,.rule::after{content:"";position:absolute;top:-2px;width:6px;height:6px;border-radius:50%;background:var(--line)}
.rule::before{left:0}.rule::after{right:0}
.about-title{position:absolute;left:635px;top:185px;font-size:45px}
.about-sub{position:absolute;left:635px;top:290px;font-size:27px;font-weight:500}
.about-copy{position:absolute;left:635px;top:352px;width:423px;font-size:13.3px;line-height:27px;text-align:justify}
.partners{position:absolute;top:1480px;left:0;width:1200px;height:900px;background:var(--cream)}
.center-title{position:absolute;left:0;width:1200px;text-align:center;font-size:56px}
.offer-box{position:absolute;left:90px;top:252px;width:775px;height:506px;background:var(--olive)}
.offer-copy{position:absolute;left:40px;top:116px;width:450px;color:var(--white);font-size:16.5px;line-height:31.5px;text-align:center}
.ring{position:absolute;left:620px;top:252px;width:510px;height:506px;border-radius:50%;background:linear-gradient(90deg,var(--ring) 50%,var(--cream) 50%)}
.ring-art{position:absolute;left:45px;top:43px;width:420px;height:420px;border-radius:50%;background:linear-gradient(180deg,#c9a3b8 0%,#e8b58d 35%,#c98a62 55%,#9b8a55 75%,#7f7445 100%)}
.benefits{position:absolute;top:2380px;left:0;width:1200px;height:1070px;background:var(--white)}
.card{position:absolute;width:218px;height:283px;background:var(--white);border-radius:40px 0 40px 0;box-shadow:0 3px 12px rgba(0,0,0,.13)}
.card svg{position:absolute;left:61px;top:46px}
.card p{position:absolute;top:162px;left:0;width:100%;text-align:center;font-size:19.5px;line-height:25px;color:var(--olive);font-weight:500;padding:0 10px}
.contact{position:absolute;top:3450px;left:0;width:1200px;height:530px;background:linear-gradient(180deg,#5f5528 0%,#5a5226 50%,#4f4a22 100%)}
.contact-art{position:absolute;inset:0;background:radial-gradient(ellipse at 50% 60%,rgba(120,105,55,.55),transparent 70%)}
.contact .center-title{color:var(--white);top:125px;font-weight:500}
.c-item{position:absolute;display:flex;align-items:center;gap:17px;color:var(--white);font-size:19px}
.c-icon{width:74px;height:74px;border-radius:50%;background:#f1e6c8;display:flex;align-items:center;justify-content:center;flex:none}
.c-item b{display:block;font-weight:500;font-size:20px;line-height:22px}
.footer{position:absolute;top:3980px;left:0;width:1200px;height:310px;background:var(--cream)}
.f-name{position:absolute;top:80px;width:1200px;text-align:center;font-size:25px;color:var(--ink)}
.f-info{position:absolute;top:160px;display:flex;gap:14px;font-size:12px;line-height:16px;color:#333}
.f-pin{width:24px;height:24px;background:var(--olive);border-radius:4px;display:flex;align-items:center;justify-content:center;flex:none;margin-top:3px}
.f-sep{position:absolute;top:235px;left:150px;width:900px;height:1px;background:#c9c6b6}
.f-nav{position:absolute;top:262px;left:0;width:1200px;display:flex;justify-content:center;gap:46px;font-size:14px}
.bottom-bar{position:absolute;top:4290px;left:0;width:1200px;height:61px;background:var(--olive)}
.copyright{position:absolute;left:75px;top:22px;color:var(--white);font-size:11.5px}
.socials{position:absolute;left:988px;top:16px;display:flex;gap:6px}
.socials span{width:30px;height:30px;border:1px solid var(--white);border-radius:3px}
</style>
</head>
<body>

<header class="site-header">
  <div class="brand">Larkmoor Capital Partners</div>
  <nav class="nav"><span class="active">HOME</span><span>ABOUT US</span><span>OUR PARTNERS</span><span>CONTACT US</span></nav>
</header>

<section class="hero">
  <div class="hero-kicker">Welcome To</div>
  <h1 class="hero-title">LARKMOOR<br>CAPITAL</h1>
  <div class="hero-sub">Partners</div>
  <div class="btn" style="left:110px;top:431px;width:175px;height:53px">Know More</div>
  <div class="hero-frame"><div class="hero-art" role="img" aria-label="Saguaro cactus in a desert landscape at sunset"></div></div>
  <div class="dots"><span class="on"></span><span></span><span></span><span></span></div>
</section>

<section class="about">
  <div class="photo-frame"><div class="photo-bg"></div></div>
  <div class="photo" role="img" aria-label="Headshot of founder Dale Corwith"></div>
  <h2 class="section-head about-title">About Us</h2>
  <div class="rule" style="left:635px;top:253px;width:150px"></div>
  <h3 class="about-sub">Meet the Founder</h3>
  <p class="about-copy">Dale Corwith is a private equity investor providing significantly above market returns to his investment partners while taking the time to be involved with his community and family. Dale first honed his skills in taking calculated risk decisions while very young where he took on playing poker professionally.</p>
  <div class="btn" style="left:635px;top:519px;width:157px;height:53px;font-size:14px">READ MORE</div>
</section>

<section class="partners">
  <h2 class="section-head center-title" style="top:97px">Our Partners</h2>
  <div class="rule" style="left:525px;top:172px;width:150px"></div>
  <div class="offer-box">
    <p class="offer-copy">Our investors offer an opportunity to families that cannot usually get approved for a mortgage, to be able to become future homeowners. Thus, Benefiting both the investors and local surrounding community members. Our investors get to both have all the benefits of an investment with receiving above market rates of return to themselves and helping families find homes at the same time.</p>
  </div>
  <div class="ring"><div class="ring-art" role="img" aria-label="Saguaro cactus against desert mesas"></div></div>
</section>

<section class="benefits">
  <h2 class="section-head center-title" style="top:110px">Our Benefits</h2>
  <div class="rule" style="left:525px;top:188px;width:150px"></div>

  <div class="card" style="left:128px;top:272px">
    <svg width="96" height="96" viewBox="0 0 96 96"><circle cx="48" cy="48" r="47" fill="#47421f"/><circle cx="48" cy="48" r="41" fill="none" stroke="#fff" stroke-width="2"/><path d="M48 24l18 7v15c0 12-8 20-18 25-10-5-18-13-18-25V31z" fill="none" stroke="#fff" stroke-width="2.5"/><path d="M40 48l6 6 11-12" fill="none" stroke="#fff" stroke-width="2.5"/></svg>
    <p>SAFETY</p></div>
  <div class="card" style="left:370px;top:272px">
    <svg width="96" height="96" viewBox="0 0 96 96"><circle cx="48" cy="48" r="47" fill="#47421f"/><circle cx="48" cy="48" r="41" fill="none" stroke="#fff" stroke-width="2"/><path d="M48 24l18 7v15c0 12-8 20-18 25-10-5-18-13-18-25V31z" fill="none" stroke="#fff" stroke-width="2.5"/><rect x="40" y="46" width="16" height="13" rx="2" fill="none" stroke="#fff" stroke-width="2.5"/><path d="M43 46v-4a5 5 0 0110 0v4" fill="none" stroke="#fff" stroke-width="2.5"/></svg>
    <p>SECURITY</p></div>
  <div class="card" style="left:612px;top:272px">
    <svg width="96" height="96" viewBox="0 0 96 96"><circle cx="48" cy="48" r="47" fill="#47421f"/><circle cx="48" cy="48" r="41" fill="none" stroke="#fff" stroke-width="2"/><circle cx="50" cy="40" r="10" fill="none" stroke="#fff" stroke-width="2.5"/><text x="50" y="45" font-size="13" text-anchor="middle" fill="#fff" font-family="Poppins,sans-serif">$</text><path d="M26 62h8l8 3h10l14-8" fill="none" stroke="#fff" stroke-width="2.5"/><path d="M50 22v-4M42 24l-2-3M58 24l2-3" stroke="#fff" stroke-width="2"/></svg>
    <p>LONG-TERM INVESTMENT HORIZON</p></div>
  <div class="card" style="left:853px;top:272px">
    <svg width="96" height="96" viewBox="0 0 96 96"><circle cx="48" cy="48" r="47" fill="#47421f"/><circle cx="48" cy="48" r="41" fill="none" stroke="#fff" stroke-width="2"/><path d="M30 44a18 18 0 0131-10M66 52a18 18 0 01-31 10" fill="none" stroke="#fff" stroke-width="2.5"/><path d="M61 26v8h-8M35 70v-8h8" fill="none" stroke="#fff" stroke-width="2.5"/><circle cx="48" cy="48" r="11" fill="none" stroke="#fff" stroke-width="2.5"/><text x="48" y="54" font-size="15" text-anchor="middle" fill="#fff" font-family="Poppins,sans-serif">$</text></svg>
    <p>CASHFLOW</p></div>

  <div class="card" style="left:250px;top:598px">
    <svg width="96" height="96" viewBox="0 0 96 96"><circle cx="48" cy="48" r="47" fill="#47421f"/><circle cx="48" cy="48" r="41" fill="none" stroke="#fff" stroke-width="2"/><rect x="34" y="24" width="30" height="40" rx="2" fill="none" stroke="#fff" stroke-width="2.5"/><text x="45" y="35" font-size="8" text-anchor="middle" fill="#fff" font-family="Poppins,sans-serif">TAX</text><path d="M44 44h14M44 50h14M44 56h14" stroke="#fff" stroke-width="2"/><circle cx="36" cy="62" r="7" fill="#47421f" stroke="#fff" stroke-width="2.5"/><path d="M33 62l2 2 4-4" fill="none" stroke="#fff" stroke-width="2"/></svg>
    <p>TAX BENEFITS</p></div>
  <div class="card" style="left:492px;top:598px">
    <svg width="96" height="96" viewBox="0 0 96 96"><circle cx="48" cy="48" r="47" fill="#47421f"/><circle cx="48" cy="48" r="41" fill="none" stroke="#fff" stroke-width="2"/><circle cx="48" cy="50" r="20" fill="none" stroke="#fff" stroke-width="2.5" stroke-dasharray="90 12"/><path d="M38 62v-6M44 62v-10M50 62v-14M56 62v-18" stroke="#fff" stroke-width="3"/><path d="M58 28l6 2-3 5" fill="none" stroke="#fff" stroke-width="2"/></svg>
    <p>ABOVE MARKET RATE OF RETURN</p></div>
  <div class="card" style="left:733px;top:598px">
    <svg width="96" height="96" viewBox="0 0 96 96"><circle cx="48" cy="48" r="47" fill="#47421f"/><circle cx="48" cy="48" r="41" fill="none" stroke="#fff" stroke-width="2"/><rect x="30" y="54" width="6" height="10" fill="none" stroke="#fff" stroke-width="2"/><rect x="40" y="48" width="6" height="16" fill="none" stroke="#fff" stroke-width="2"/><rect x="50" y="42" width="6" height="22" fill="none" stroke="#fff" stroke-width="2"/><rect x="60" y="34" width="6" height="30" fill="none" stroke="#fff" stroke-width="2"/><circle cx="42" cy="34" r="7" fill="none" stroke="#fff" stroke-width="2"/><text x="42" y="38" font-size="10" text-anchor="middle" fill="#fff" font-family="Poppins,sans-serif">$</text><path d="M54 34l12-10M60 24h6v6" fill="none" stroke="#fff" stroke-width="2"/></svg>
    <p>CAPITAL GROWTH</p></div>
</section>

<section class="contact">
  <div class="contact-art" role="img" aria-label="Faded saguaro desert backdrop"></div>
  <h2 class="center-title">Contact Us</h2>
  <div class="rule" style="left:525px;top:210px;width:150px;background:#e8e2c8"></div>
  <div class="c-item" style="left:261px;top:248px">
    <div class="c-icon"><svg width="36" height="26" viewBox="0 0 36 26"><rect x="1" y="1" width="34" height="24" rx="2" fill="none" stroke="#47421f" stroke-width="2.5"/><path d="M2 2l16 13L34 2M2 24l12-10M34 24L22 14" fill="none" stroke="#47421f" stroke-width="2.5"/></svg></div>
    <div><b>EMAIL US</b>Dale@LarkmoorFunds.example</div>
  </div>
  <div class="c-item" style="left:705px;top:248px">
    <div class="c-icon"></div>
    <div>@DaleCorwith</div>
  </div>
  <div class="c-item" style="left:261px;top:368px">
    <div class="c-icon"></div>
    <div>https://www.profilehub.example/in/dale-corwith-58172036/</div>
  </div>
</section>

<footer class="footer">
  <div class="f-name">Larkmoor Capital Partners</div>
  <div class="f-info" style="left:225px"><div class="f-pin"><svg width="12" height="12" viewBox="0 0 12 12"><path d="M2 1l3 0 1 3-2 1a7 7 0 003 3l1-2 3 1v3c-6 0-10-4-10-9z" fill="#fff"/></svg></div><div>CALL US<br>8012 555 0193</div></div>
  <div class="f-info" style="left:443px"><div class="f-pin"><svg width="12" height="9" viewBox="0 0 12 9"><rect width="12" height="9" fill="#fff"/><path d="M0 0l6 5 6-5" fill="none" stroke="#47421f"/></svg></div><div>EMAIL US<br>info@larkmoorfunds.example</div></div>
  <div class="f-info" style="left:731px"><div class="f-pin"><svg width="10" height="13" viewBox="0 0 10 13"><path d="M5 13S0 7 0 5a5 5 0 0110 0c0 2-5 8-5 8z" fill="#fff"/><circle cx="5" cy="5" r="2" fill="#47421f"/></svg></div><div>Address line Dummy Here<br>Address line Here</div></div>
  <div class="f-sep"></div>
  <nav class="f-nav"><span>HOME</span><span>ABOUT US</span><span>OUR PARTNERS</span><span>CONTACT US</span></nav>
</footer>

<div class="bottom-bar">
  <div class="copyright">Copyright © 2024 All Rights Reserved By Larkmoor Capital Partners</div>
  <div class="socials"><span></span><span></span><span></span><span></span></div>
</div>

</body>
</html>
```